Orbit 582 - Kindle Book Cover

I am looking for a Kindle book cover for my book about "Orbit 582".
The Book is Titled:
Orbit 582 Ascended
Shaping Tomorrow: Paths To Unlocking Hidden Currents
Author is Dorian Welby
Here is a book description that may help you understand more about it:
Inspired by the genius of Bertram Ollinger, this comprehensive guide delves into the ancient wisdom and cutting-edge science behind the 582 method, a powerful tool for manifesting your desires. Whether you're seeking personal growth, financial success, or spiritual enlightenment, this book provides advanced techniques and methods to transform your dreams into reality.
Any questions please ask.
Thanks
Gavin

```html
<!DOCTYPE html>
<html lang="en">
<head>
<meta charset="utf-8">
<title>Orbit 582 Ascended — Dorian Welby</title>
<link rel="stylesheet" href="https://fonts.googleapis.com/css2?family=Old+Standard+TT:wght@400;700&display=swap">
<style>
  :root {
    --sky-top: #020309;
    --sky-deep: #010c22;
    --sky-mid: #02234f;
    --sky-low: #0f4a78;
    --cloud-blue: #3f86ad;
    --cloud-light: #8fbfd6;
    --ink-light: #ffffff;
  }
  html, body {
    margin: 0;
    padding: 0;
    width: 800px;
    height: 1200px;
    overflow: hidden;
    background: var(--sky-top);
  }
  .book-cover {
    position: relative;
    width: 800px;
    height: 1200px;
    overflow: hidden;
    font-family: "Old Standard TT", "Times New Roman", serif;
    color: var(--ink-light);
  }
  .cover-art {
    position: absolute;
    inset: 0;
    background:
      radial-gradient(ellipse 70% 25% at 30% 88%, rgba(143,191,214,0.75), rgba(143,191,214,0) 70%),
      radial-gradient(ellipse 45% 18% at 72% 92%, rgba(143,191,214,0.6), rgba(143,191,214,0) 70%),
      linear-gradient(180deg,
        var(--sky-top) 0%,
        var(--sky-deep) 35%,
        var(--sky-mid) 50%,
        var(--sky-low) 64%,
        var(--cloud-blue) 80%,
        var(--cloud-light) 100%);
  }
  .cover-text {
    position: absolute;
    inset: 0;
    text-align: center;
  }
  .book-title {
    position: absolute;
    top: 352px;
    left: 0;
    right: 0;
    margin: 0;
    font-weight: 700;
    font-size: 92px;
    line-height: 100px;
    letter-spacing: 2px;
    text-transform: uppercase;
  }
  .book-subtitle {
    position: absolute;
    top: 584px;
    left: 0;
    right: 0;
    margin: 0;
    font-weight: 400;
    font-size: 39px;
    line-height: 51px;
    letter-spacing: 0.5px;
  }
  .book-author {
    position: absolute;
    top: 1080px;
    left: 0;
    right: 0;
    margin: 0;
    font-weight: 400;
    font-size: 31px;
    letter-spacing: 1px;
    text-transform: uppercase;
  }
</style>
</head>
<body>
  <main class="book-cover">
    <div class="cover-art" role="img" aria-label="Night sky full of stars fading from black into deep blue, with soft pale blue clouds along the bottom"></div>
    <div class="cover-text">
      <h1 class="book-title">Orbit 582<br>Ascended</h1>
      <p class="book-subtitle">Shaping Tomorrow: Paths to<br>Unlocking Hidden Currents</p>
      <p class="book-author">Dorian Welby</p>
    </div>
  </main>
</body>
</html>
```